Need a corporate background Image with our existing logo for Zoom or Microsoft Teams

Hi,

We require a corporate background image with our existing logo use with Zoom or Microsoft Teams.

Our existing logo is at https://www.halvenrock-systems.com/images/logo_top.png

Thank you.

```html
<!DOCTYPE html>
<html lang="en">
<head>
<meta charset="utf-8">
<title>Halvenrock Systems – Video Call Background</title>
<link href="https://fonts.googleapis.com/css2?family=Archivo:wght@800&display=swap" rel="stylesheet">
<style>
  :root {
    --sky-top: #f7f9fc;
    --sky-mid: #eef4fb;
    --haze: #dcebfa;
    --glow-blue: #9cc8f2;
    --deep-blue: #3d8fe0;
    --line-blue: #5aa2ea;
    --brand-blue: #1a73c9;
  }
  html, body {
    margin: 0;
    padding: 0;
    width: 1200px;
    height: 675px;
    overflow: hidden;
    background: #ffffff;
  }
  .call-background {
    position: relative;
    width: 1200px;
    height: 675px;
    overflow: hidden;
    background: radial-gradient(ellipse at 50% 30%, #ffffff 0%, var(--sky-top) 40%, var(--sky-mid) 75%, var(--haze) 100%);
  }
  .frame-lines {
    position: absolute;
    inset: 0;
    width: 1200px;
    height: 675px;
  }
  .brand {
    position: absolute;
    left: 92px;
    top: 52px;
    display: flex;
    align-items: center;
    gap: 14px;
    font-family: "Archivo", "Arial Black", sans-serif;
    font-weight: 800;
    color: var(--brand-blue);
  }
  .brand-mark {
    width: 46px;
    height: 46px;
    border-radius: 50%;
    background: var(--brand-blue);
  }
  .brand-name {
    display: flex;
    flex-direction: column;
    line-height: 1;
  }
  .brand-name .primary {
    font-size: 34px;
    letter-spacing: 0.5px;
  }
  .brand-name .secondary {
    font-size: 13px;
    letter-spacing: 7px;
    margin-top: 8px;
  }
</style>
</head>
<body>
  <main class="call-background">
    <svg class="frame-lines" viewBox="0 0 1200 675" aria-hidden="true">
      <defs>
        <linearGradient id="floorLeft" x1="0" y1="0" x2="1" y2="0">
          <stop offset="0" stop-color="#7fb8ee" stop-opacity="0.8"/>
          <stop offset="1" stop-color="#cfe3f7" stop-opacity="0"/>
        </linearGradient>
        <linearGradient id="floorRight" x1="1" y1="0" x2="0" y2="0">
          <stop offset="0" stop-color="#7fb8ee" stop-opacity="0.8"/>
          <stop offset="1" stop-color="#cfe3f7" stop-opacity="0"/>
        </linearGradient>
        <linearGradient id="bandFade" x1="0" y1="0" x2="0" y2="1">
          <stop offset="0" stop-color="#ffffff" stop-opacity="0"/>
          <stop offset="1" stop-color="#b8d8f5" stop-opacity="0.9"/>
        </linearGradient>
      </defs>

      <!-- lower side glow -->
      <rect x="0" y="380" width="1200" height="295" fill="url(#bandFade)"/>
      <polygon points="0,430 330,520 330,560 0,600" fill="url(#floorLeft)" opacity="0.55"/>
      <polygon points="1200,430 870,520 870,560 1200,600" fill="url(#floorRight)" opacity="0.55"/>
      <polygon points="0,560 320,600 320,620 0,620" fill="#ffffff" opacity="0.6"/>
      <polygon points="1200,560 880,600 880,620 1200,620" fill="#ffffff" opacity="0.6"/>
      <polygon points="0,585 320,565 320,580 0,615" fill="var(--deep-blue)" opacity="0.35"/>
      <polygon points="1200,585 880,565 880,580 1200,615" fill="var(--deep-blue)" opacity="0.35"/>

      <!-- frame lines -->
      <g fill="none" stroke="var(--line-blue)" stroke-width="1" opacity="0.75">
        <polyline points="47,0 47,200 78,275 244,340 345,455"/>
        <polyline points="1153,0 1153,200 1122,275 956,340 855,455"/>
        <polyline points="40,400 220,440 250,470" opacity="0.5"/>
        <polyline points="1160,400 980,440 950,470" opacity="0.5"/>
      </g>

      <!-- floor perspective lines -->
      <g stroke="var(--deep-blue)" stroke-width="1.2" opacity="0.6">
        <line x1="90" y1="675" x2="320" y2="585"/>
        <line x1="1110" y1="675" x2="880" y2="585"/>
        <line x1="0" y1="640" x2="300" y2="575"/>
        <line x1="1200" y1="640" x2="900" y2="575"/>
      </g>
    </svg>

    <div class="brand">
      <span class="brand-mark" aria-hidden="true"></span>
      <span class="brand-name">
        <span class="primary">HALVENROCK</span>
        <span class="secondary">SYSTEMS</span>
      </span>
    </div>
  </main>
</body>
</html>
```